Web Design Home Page

KRVL Athletics.com – Homepage Vision
KRVL is a community based youth sports program currently running basketball and soccer programs. We run recreational leagues, competitive club programs and run many camps, clinics and development programs in both sports.
My vision on the KRVL Home page was to design a clean page that will guide viewers quickly to the sport of interest.
At the top I was thinking of a KRVL Logo Bar. I want something that we can also customize for each of the sports to use in the future. So, 5 different logo bars.
1 – KRVL Athletics Logo Bar – Goes on the KRVLAthletics.com home page, which give general information about the club as a whole and leads folks to the sport they want to go.
2 – KRVL Basketball – Recreational. Same look as the homepage logo bar but only contains info regarding to recreational basketball.
3 – KRVL Basketball – Competitive. Same as above but only competitive basketball.
4 – KRVL Soccer – Recreational. Same as above but only recreational soccer.
5 – KRVL Soccer – Competitive. Same as above but only competitive soccer.
Maybe the logo bar on the home page can also be the main logo bar and also rotate the other 4 underneath the main logo bar. Logo are old, may need to be updated at some point.
The middle section, I was thinking of 4 boxes that when clicked on will take you to the appropriate website. The designs I used are just to show something. I took the picture off the web and they may be copyrighted so would probably need some type of original designs.
Recreational Basketball Website - http://krvlathletics-example.com/basketball/index.html
Competitive Basketball Website - http://www.krvlherons-example.com/
Recreational Soccer Website - http://krvlathletics-example.com/soccer/index.html
Competitive Soccer Website - http://www.ridgepremiersoccer-example.com/
Recreational basketball uses Granite Mesa Basketball (we own the trade name) or KRVL Basketball.
The competitive basketball club is known as KRVL Herons.
Recreational soccer goes by Granite Mesa Soccer or Granite Mesa Soccer Club.
Competitive soccer goes by Ridge Premier Soccer or Granite Mesa Soccer Club.
Then on the bottom of the page I was thinking of a menus bar that contains information general to the club (both basketball and soccer). When you click on any a pop up box will pop up with the information for each listed below.
About Us
Granite Mesa Athletic Club provides recreational leagues for both Basketball and Soccer with the focus placed on providing our youth with the rewarding opportunity of participating in youth sports. Our direction is to promote the recreational value of youth sports while emphasizing fun and respect for the sport.
Granite Mesa Athletic Club (KRVL) is based in the North Phoenix area with most of our players residing in the Willow Bend School District.
Our Mission
Our mission at Granite Mesa Athletic Club is to promote and develop excellence in youth sports based on skill, sportsmanship, values, and player character. Our programs aim to provide an environment for natural player development that prepares them for life experiences, both on and off the field.
We focus on a uniform sports philosophy throughout the club that emphasizes growth through positive reinforcement resulting in players achieving his/her fullest potential. We do not look for the next victory to measure our success, but in the total learning experience for each player, realizing that the team is much stronger than an individual.
Contact Info
Granite Mesa Athletic Club
P.O. Box 7068
Willow Bend, AZ 85990
Club Phone – 480-555-0173
Club Website – KRVLAthletics.com
Club Email – info@krvlathletics-example.com
Basketball Email – KRVLBB@mail-example.com
Soccer Email – KRVLSoccer@mail-example.com
Our Mission
The mission of KRVL shall be to promote good citizenship and health through community athletic activities for children and for educational purposes. Club focus is on player development, with emphasis on teamwork and sportsmanship with high standards for both parents and players. Respect, commitment and accountability are qualities we ask all our members to endorse both on and off the field.

```html
<!DOCTYPE html>
<html lang="en">
<head>
<meta charset="utf-8">
<title>KRVL 2013 Competitive Team Tryouts</title>
<link rel="stylesheet" href="https://fonts.googleapis.com/css2?family=Audiowide&family=Cabin:wght@400;700&display=swap">
<style>
  :root {
    --page-bg: #d9d9d9;
    --page-bg-light: #e6e6e6;
    --band-green: #5c7a42;
    --band-green-dark: #4a6634;
    --sidebar-green: #4e6c36;
    --sidebar-green-dark: #425d2d;
    --panel-green: #8fa877;
    --tile-green: #86a96b;
    --footer-green: #7b9a62;
    --white: #ffffff;
    --note-red: #e3120b;
    --frame-dark: #333333;
  }
  * { box-sizing: border-box; margin: 0; padding: 0; }
  html, body { width: 1200px; height: 675px; overflow: hidden; }
  body {
    position: relative;
    background: radial-gradient(ellipse at 50% 40%, var(--page-bg-light), var(--page-bg) 70%);
    font-family: "Cabin", sans-serif;
  }
  .title-band {
    position: absolute; left: 0; top: 38px; width: 1200px; height: 50px;
    background: linear-gradient(var(--band-green), var(--band-green-dark));
    box-shadow: 0 3px 5px rgba(0,0,0,0.35);
  }
  .page-title {
    position: absolute; left: 420px; top: 48px; width: 730px; text-align: center;
    font-family: "Audiowide", sans-serif; font-size: 29px; color: var(--white);
    letter-spacing: 0.5px;
  }
  .sidebar {
    position: absolute; left: 302px; top: 86px; width: 105px; height: 451px;
    background: linear-gradient(90deg, var(--sidebar-green-dark), var(--sidebar-green) 50%, var(--sidebar-green-dark));
    box-shadow: 0 2px 5px rgba(0,0,0,0.35);
  }
  .club-mark {
    position: absolute; left: 318px; top: 50px; width: 74px; height: 84px;
    display: flex; flex-direction: column; align-items: center;
  }
  .club-mark .badge-circle {
    width: 60px; height: 60px; border-radius: 50%;
    border: 3px solid var(--white);
  }
  .club-mark .club-name {
    margin-top: 4px; font-weight: 700; font-size: 12px; color: var(--white); letter-spacing: 1px;
  }
  .main-nav {
    position: absolute; left: 302px; top: 146px; width: 105px; list-style: none;
  }
  .main-nav li {
    height: 37.3px; display: flex; align-items: center; justify-content: center;
    font-size: 9px; font-weight: 700; color: var(--white); text-align: center;
  }
  .main-nav li.current { background: rgba(255,255,255,0.06); }
  .program-tile {
    position: absolute; left: 237px; width: 62px; height: 61px;
    background: var(--tile-green); border: 2px solid #d9e3cf;
    box-shadow: 0 1px 3px rgba(0,0,0,0.3);
  }
  .program-tile .ball-art {
    position: absolute; left: 5px; top: 5px; width: 46px; height: 46px;
    border-radius: 50%; background: radial-gradient(circle, #eef3e9, #c9d8bd);
  }
  .program-tile .tier {
    position: absolute; right: 3px; bottom: 1px; font-size: 8px; font-weight: 700; color: var(--white);
  }
  .content-panel {
    position: absolute; left: 425px; top: 88px; width: 537px; height: 449px;
    background: var(--panel-green); box-shadow: 0 2px 5px rgba(0,0,0,0.3);
  }
  .photo-slot {
    position: absolute; left: 443px; top: 172px; width: 289px; height: 177px;
    background: var(--white); border: 1px solid var(--frame-dark);
  }
  .tryout-copy {
    position: absolute; left: 752px; top: 171px; width: 128px;
    font-size: 11px; font-weight: 700; line-height: 13.2px; color: var(--white);
  }
  .footer-bar {
    position: absolute; left: 217px; top: 546px; width: 766px; height: 32px;
    background: var(--footer-green); border-bottom: 3px solid #c6d3ba;
    box-shadow: 0 2px 4px rgba(0,0,0,0.3);
  }
  .social-links {
    position: absolute; right: 38px; top: 8px; display: flex; gap: 14px; list-style: none;
  }
  .social-links li { font-size: 12px; font-weight: 700; color: var(--white); }
  .design-note {
    position: absolute; left: 1010px; top: 137px; width: 190px; text-align: center;
    font-size: 13px; line-height: 18.2px; color: var(--note-red);
  }
</style>
</head>
<body>
  <header class="title-band"></header>
  <h1 class="page-title">KRVL 2013 Competitive Team Tryouts</h1>

  <nav class="sidebar" aria-label="Main navigation"></nav>
  <div class="club-mark">
    <span class="badge-circle"></span>
    <span class="club-name">KRVL</span>
  </div>
  <ul class="main-nav">
    <li>Announcement</li>
    <li>Teams</li>
    <li>Player Expectations</li>
    <li class="current">Try outs</li>
    <li>Training Staff</li>
    <li>FAQ</li>
    <li>Contact us</li>
  </ul>

  <a class="program-tile" style="top:112px"><span class="ball-art" role="img" aria-label="Basketball icon for recreational basketball"></span><span class="tier">R</span></a>
  <a class="program-tile" style="top:203px"><span class="ball-art" role="img" aria-label="Basketball icon for competitive basketball"></span><span class="tier">C</span></a>
  <a class="program-tile" style="top:296px"><span class="ball-art" role="img" aria-label="Soccer ball icon for recreational soccer"></span><span class="tier">R</span></a>
  <a class="program-tile" style="top:391px"><span class="ball-art" role="img" aria-label="Soccer ball icon for competitive soccer"></span><span class="tier">C</span></a>

  <main class="content-panel"></main>
  <div class="photo-slot" role="img" aria-label="Space for a photo of players at tryouts"></div>
  <p class="tryout-copy">Tryouts for our competitive teams are held in August but we do have a couple of openings for the Winter season. If you are interested in competitive basketball or looking for a club team please email us the Player's Name, Grade, Age, School Attending and you contact information and put "Competitive Teams" in the subject line to the email address below, KRVLBB@mail-example.com</p>

  <footer class="footer-bar">
    <ul class="social-links">
      <li>Facenote</li>
      <li>Chirper</li>
    </ul>
  </footer>

  <p class="design-note">Once more photography would to wonders here a nice picture of some kids trying their hardest . Also if you notice the social media icons I added , those will take users to you Chirper or Facenote page (if you use any other services I will be happy to add them in) and again we have a nice roll over effect the white logo going grey.</p>
</body>
</html>
```